MENU DESIGN FOR KESARI LOOM RESTUARNT

1.NEED TRI FOLD MENU FOR TAKE OUT FRONT AND BACK JUST LIKE I HAVE ATTACHED THE MENU .....IT COULD EVEN ALMOST IDENTICAL. ( COPY THE MENU ITEMS AT THE BOTTOM OF THIS PAGE.

2. I NEED A POSTER FOR LUNCH COMBO 11AM-2PM
THRE ARE 3 COMBOS
A....HIT_____ SERVED WITH RICE AND ONE ENTREE WITH PCS OF FRESH TANDOORI NAAN BREAD IN 7" CONTAINER....13

B...SUPERHIT......SERVED WITH RICE, SALAD.NAAN, POP, AND ONE ENTREE .....$15

C...BLOCKBUSTER.....SERVED WITH RICE, SALAD, NAAN, POP, AND ONE ENTEE AND ONE ADD-ON....$18

BOTTOM OF THE PAGE PLEASE WE WILL HAVE LIST OF ENTEE + ADD WITH PRICE ...PLS NOTE WE WILL HAVE 10 ENTREE WHIS WILL ALSO TRANSLATE TO 10 ADD ON

AFTER THE DESIGN YOU CAN ATTACH THIS POSTER TO TAKEOUNT MENU WHICH WILL TAKE 1 PAGE.

HER IS THE TAKE OUT MENU ITEMS IN SECTIONS

TANDOORI DINNERS for meat lovers….
Served with rice, salad, roti or naan.

"Signature" BONELESS CHICKEN TIKKA ……………………………
-appetizer $10 / single dinner $15/ big dinner $20
boneless diced chicken marinated with KL secret masala and cooked in tandoor.

"Haryali" BONELESS CHICKEN TIKKA ……………………………………
10/15/20
boneless dice chicken marinated with mint and cilantro cooked in tandoor

"Malai" BONELESS CHICKEN TIKKA…………………………………………………………………
10/15/20
boneless diced chicken marinated with cheese, yogurt and mild spices and cooked in tandoor

"Hot n Spicy" BONELESS CHICKEN TIKKA……………………………………………………………………….
12/17/25
boneless dice chicken marinated with hot spices and cooked in tandoor.

CHICKEN SEEKH KABOB…………………………………………………………………10/15/20

minced ground chicken cooked in tandoor

TANDOORI CHICKEN bone-in……………………………………………………………………………10/15/20
chicken pcs marinated in seasoning and cooked in tandoor.……………………

TANDOORI CHICKEN LEGS

8/10/18

marinated chicken legs cooked in tandoor

TANDOORI CHICKEN WINGS

8/10/18

marinated chicken wings cooked in the tandoor

LAMB CHOPS KABOB……………………………………………………………………

18/22/32

marinated lamb chops in blended spices cooked in tandoor.

SHOULDER LAMB CHOP KEBOB

15/20/30

FISH TIKKA ………………………………………………………………………………………………15/20/32

Moist & tender spice marinated chunks of Salmon cooke in tandoor

TANDOOR SHRIMP………………………………………………………………

17/20/35

marinated shrimp cooked in tandoor.

TANDOORI PANEER TIKKA

10/15/20

chanks of paneer marinated in spices cooked in a tandoor

TANDOORI VEG. KEBOBS

10/15/20

marinated fresh vegetables cooked in a tandoor

**********+++++++=====

—————————TANDOORI KEBOB PLATERS————————————————

4 PERSON $32 6 PERSON $42 8 PERSON $50

———————————TANDOORI WRAPS———————————————————

CHICKEN TIKKA KEBOB WRAP $10
CHICKEN SEEKH KEBOB WRAPS $10
“HOT & SPICY” CHICKEN TIKKA WRAP $12
SALMON FISH TIKKA WRAP
PANEER TIKKA WRAP

VEGETARIAN MAIN COURSE CURRIES SMALL MEDIUM LARGE

CHANNA MASALA $6 $10 $15

DAAL MAKHANI 8 12 17

PANEER MAKHANI 8 12 17

KARAHI PANEER 8 12 17

PALAK PANEER 8 12 17

CHILLIE PANEER 9 13 18

BENGAN AFGHANI 9 12 17

BENGAN BHARTHA 8 12 17

MIX VEG. 8 12 17

VEG. MANCHURIAN 10 14 18

==========SIDES========
TAWA ROTI $1.50
TANDOORI ROTI $1.75
TANDOORI BUTTER NAAN $2
TANDOORI PLAIN NAAN $1.75
TANDOORI GARLIC NAAN $2.50
PLAIN PARATHA $2.50
TAWA NAAN $3.00
BATURA $1.50

BASMATI RICE SMALL $3.50SM LARGE $5
SALAD $3.50
SALAD UPGRADE $4.75
MASALA FRIES
RAITA $3.50

=============== PLATER / ROLL 12PM-4PM =============

2 VEG. CURRY+NAAN+RICE $10
1 VEG. CURRY+NAAN+RICE $8.50
VEG. CURRY ON RICE $7.50

CHANNA / KADAI PANEER / PALAK PANEER / PALAK PANEER / MIX VEG. $8

MEAT LOVERS MAIN COURSE CURRIES

BONELESS BUTTER CHICKEN……………………………………………………………
S $11 ……M15…….L24
diced boneless tandoori chicken cooked in butter and creamy sauce.

KADAI CHICKEN MASALA…………………………………………………………………
S$11……..M$15……..L24
boneless chicken cooked in spices and thick gravy.

CHICKEN TIKKA MASALA………………………………………………………………………………11/15/24
tandoori chicken tikka cooked with spice and gravy.

CHICKEN KOFTA CURRY………………………………………………………………………………11/15/24
chicken kofta cooked in tomatoes and spices.

AFGHANI CHICKEN HARYALI…………………………………………………………………………………11/15/24
chicken cooked with spinach and spices.

CHICKEN VINDALOO……………………………………………………………………………
12/18/29
boneless chicken cooked with potatoes & spices in a thick gravy.

CHICKEN CURRY…..

11/15/24

boneless chicken cooked in the soup gravy

CHILLIE CHICKEN WITHG RAVY

12/18/29

METHI MALAI CHICKEN

11/15/24

boneless chicken cooked cheese and methi

LAMB VINDALOO……………………………………………………………………

13/20/29

boneless lamb cooked with potatoes & spices in a thick gravy.

AFGHANI HARYALI LAMB………………………………………………………………………
13/20/29
lamb cooked with spinach and spices.

SHRIMP VINDALOO……………………………………………………………………
13/20/29
shrimp cooked in the thick spicy sauce.

TANDOORI SHRIMP MASALA

15/25/32

FISH TIKKA MASALA…………………………………………………………………………

15/20/32

fish in spicy curry sauce.

SPECIAL MEALS

LAMB BIRYANI……………………………………………………………………………………………………………..$10

lamb seasoned with fragrant spices and fresh herbs.

CHICKEN BIRYANI…………………………………………………………………………………………………………$9
chicken seasoned with fragrant spices and fresh herbs cooked with rice.

check out our website www.kesariloom.ca FOR

SPCIALS DAILY
SPECIAL ORDERS MENU
DESSRT MENU
DRINK MENU
DESSERT MENU

BENGAN BHARTA
comprises bhurtha (minced vegetables) made from eggplant (baingan) which is grilled over charcoal or direct fire, to infuse the dish with a smoky flavour

PANEER MAKHANI
COTTAGE CHEESE COOKED WITH BUTTER AND CREAMY SAUCE.

VEG. MANCHURIAN AND CHILLIE PANEER- PLS KEEP AT THE SAME PLACE

PLS KEEP VEG SNACKS WITH PRICE CHANGE

ALL VEG SAME WITH PRICE

Target Market(s)

PEOPLE WHO LOVE FRESH INDIAN FOOD

Font styles to use
Decorative
Script

Colors
ec1f27
fdf1e7
f68e4e
fbed22
ffcf3e
faa54b
f68d4c
e34197

Requirements
Must have
• LOGO
• SIZES
• PRICE
• SOME VISUAL
• FILM OR MOVIE THEME
• ACTOR DIRECTOR CINEMA FEEL
Nice to have
• CURRY COMBOS IN FILM REEL NICE TO HAVE BUT NOT A MUS AS I M LOOKING FOR MORE ELEGANT DESIGN NOT A CARTOONI OR BUSY
• MUST BE PROFESSIONAL LOOK
• SIMPLE
• EASY
• ATTRACTIVE

```html
<!DOCTYPE html>
<html lang="en">
<head>
<meta charset="utf-8">
<title>Kesari Loom – Lunch Combos</title>
<link rel="stylesheet" href="https://fonts.googleapis.com/css2?family=Bungee&family=Michroma&family=Arimo:wght@400;700&display=swap">
<style>
  :root{
    --backdrop:#e4d6b7;
    --ink:#231f20;
    --panel-orange:#e2582b;
    --box-orange:#e8602a;
    --cream:#fdf1e7;
    --bulb:#fbe3c4;
    --muted:#bdb6b0;
  }
  *{box-sizing:border-box;margin:0;padding:0}
  html,body{width:807px;height:1200px;overflow:hidden}
  body{background:var(--backdrop);position:relative;font-family:"Arimo",Arial,sans-serif}
  .poster{position:absolute;left:167px;top:0;width:479px;height:1192px;background:var(--ink)}
  .chef-art{position:absolute;top:12px;width:96px;height:96px;border-radius:8px;
    background:radial-gradient(circle at 50% 45%,#f4f0ea 0 42%,#3a3435 70%)}
  .chef-art.left{left:10px}
  .chef-art.right{right:10px}
  .lunch-hours{position:absolute;top:22px;left:0;right:0;text-align:center;color:var(--cream);
    font-family:"Michroma",sans-serif;font-size:15px;line-height:1.35;letter-spacing:1px}
  .combos{position:absolute;top:108px;left:13px;right:13px;display:flex;gap:4px}
  .combo{flex:1;height:147px;background:var(--box-orange);border:5px dotted var(--bulb);
    padding:8px 8px;text-align:center;color:var(--cream);display:flex;flex-direction:column}
  .combo-name{font-family:"Bungee",sans-serif;font-size:25px;line-height:1;color:var(--cream)}
  .combo-name.two-line{font-size:19px}
  .combo-desc{font-size:8px;line-height:1.25;margin-top:5px;flex:1}
  .combo-price{font-family:"Bungee",sans-serif;font-size:24px;line-height:1}
  .combo-price sup{font-size:11px;vertical-align:10px}
  .menu-panel{position:absolute;left:13px;right:13px;background:var(--panel-orange);padding:0 34px}
  .menu-panel.sides{top:282px;height:404px}
  .menu-panel.entries{top:712px;height:391px}
  .menu-title{font-family:"Bungee",sans-serif;font-size:30px;text-align:center;color:var(--ink);
    margin:40px 0 24px}
  .menu-list{list-style:none}
  .menu-list li{display:flex;align-items:baseline;color:var(--ink);font-size:16.5px;line-height:24.5px}
  .menu-list .leader{flex:1;border-bottom:2px dotted var(--ink);margin:0 3px;transform:translateY(-4px)}
  .halal-note{position:absolute;top:1103px;left:0;right:0;text-align:center;color:var(--muted);font-size:9px;letter-spacing:1px}
  .footer{position:absolute;top:1122px;left:22px;right:22px;display:flex;justify-content:space-between;color:var(--cream)}
  .brand-name{font-family:"Michroma",sans-serif;font-size:17px;letter-spacing:1px;line-height:1.2}
  .brand-sub{font-family:"Michroma",sans-serif;font-size:7px;letter-spacing:4px;margin-top:1px}
  .brand-web{font-size:11px;letter-spacing:1.5px;margin-top:6px}
  .contact{text-align:left;width:190px}
  .services{font-family:"Michroma",sans-serif;font-size:9px;word-spacing:6px}
  .phone{font-family:"Michroma",sans-serif;font-size:9px;margin-top:3px}
  .contact-small{font-size:7px;line-height:1.35;margin-top:6px;color:var(--muted)}
</style>
</head>
<body>
<main class="poster">
  <div class="chef-art left" role="img" aria-label="Illustration of a chef's hat with moustache"></div>
  <div class="chef-art right" role="img" aria-label="Illustration of a chef's hat with moustache"></div>
  <p class="lunch-hours">LUNCH:<br>11PM-2PM ONLY</p>

  <section class="combos">
    <article class="combo">
      <h2 class="combo-name">HIT</h2>
      <p class="combo-desc">1 Choice of<br>Curry Or Rice</p>
      <p class="combo-price">$10<sup>.95</sup></p>
    </article>
    <article class="combo">
      <h2 class="combo-name two-line">SUPER<br>HIT</h2>
      <p class="combo-desc">1 Choice Of Curry Or Rice With One Naan &amp; Bottle Water Or Pop</p>
      <p class="combo-price">$12<sup>.95</sup></p>
    </article>
    <article class="combo">
      <h2 class="combo-name two-line">BLOCK<br>BUSTER</h2>
      <p class="combo-desc">1 Choice Of Curry Or Rice With One Naan &amp; Bottle Water Or Pop</p>
      <p class="combo-price">$16<sup>.95</sup></p>
    </article>
  </section>

  <section class="menu-panel sides">
    <h2 class="menu-title">SIDES</h2>
    <ul class="menu-list">
      <li>Naan<span class="leader"></span>$1</li>
      <li>Extra Rice<span class="leader"></span>$1</li>
      <li>Pakora(2 pcs)<span class="leader"></span>$1</li>
      <li>Lamb Chop(2 pcs)<span class="leader"></span>$3</li>
      <li>Chicken Tikka (2 PCs)<span class="leader"></span>$3</li>
      <li>Salad<span class="leader"></span>$3</li>
      <li>Sample Text<span class="leader"></span>$3</li>
      <li>Sample Text<span class="leader"></span>$3</li>
      <li>Sample Text<span class="leader"></span>$3</li>
    </ul>
  </section>

  <section class="menu-panel entries">
    <h2 class="menu-title">ENTRIES</h2>
    <ul class="menu-list">
      <li>Naan<span class="leader"></span>$1</li>
      <li>Extra Rice<span class="leader"></span>$1</li>
      <li>Pakora(2 pcs)<span class="leader"></span>$1</li>
      <li>Lamb Chop(2 pcs)<span class="leader"></span>$3</li>
      <li>Chicken Tikka (2 PCs)<span class="leader"></span>$3</li>
      <li>Salad<span class="leader"></span>$3</li>
      <li>Sample Text<span class="leader"></span>$3</li>
      <li>Sample Text<span class="leader"></span>$3</li>
      <li>Sample Text<span class="leader"></span>$3</li>
    </ul>
  </section>

  <p class="halal-note">WE SERVE HALAL</p>

  <footer class="footer">
    <div class="brand">
      <p class="brand-name">KESARI LOOM</p>
      <p class="brand-sub">RESTAURANT</p>
      <p class="brand-web">www.kesariloom.ca</p>
    </div>
    <div class="contact">
      <p class="services">DINE-IN TAKEOUT CATERING</p>
      <p class="phone">555 014 2231</p>
      <p class="contact-small">Please contact us for Complete Delivery And Catering<br>120 Marigold Avenue Unit 4 Springvale</p>
    </div>
  </footer>
</main>
</body>
</html>
```